Jan 2020 Newsletter

To send out information with some graphical representation to our clients.

Target Market(s)

Property Owners and Managers

Industry/Entity Type

Property

Colors
acd037

Requirements
Must have
• Must have branding
• www.quillmarsh.co.uk
Nice to have
• Must be information and provide facts and clear guidelines
• you can see other projects that have been done for us.
• Please refer to attachment for the information for the newsletter. This is in Word format
• Please refer to other projects we have posted on here to give an idea of what we have had in the past.

```html
<!DOCTYPE html>
<html lang="en">
<head>
<meta charset="utf-8">
<title>Quillmarsh Newsletter – January 2020</title>
<link href="https://fonts.googleapis.com/css2?family=Poppins:wght@400;500;600;700&display=swap" rel="stylesheet">
<style>
  :root{
    --green:#3db54a;
    --green-dark:#2a8f36;
    --lime:#8fcf4a;
    --amber:#ffc000;
    --red:#ff1a1a;
    --ink:#3c3c3c;
    --ink-soft:#555;
    --page:#cbcbcb;
    --panel:#efefef;
    --white:#ffffff;
    --rule:#d6d6d6;
    --head-row:#dcebf3;
  }
  *{box-sizing:border-box;margin:0;padding:0}
  html,body{width:1200px;height:5040px;overflow:hidden}
  body{background:var(--page);font-family:"Poppins",sans-serif;color:var(--ink)}
  .newsletter{position:absolute;left:214px;top:143px;width:780px;height:4765px;background:var(--panel);overflow:hidden}

  .masthead{height:180px;background:var(--white);border-bottom:7px solid var(--green);display:flex;align-items:center;justify-content:center}
  .brand-name{font-weight:600;font-size:58px;color:var(--ink);line-height:1}

  .hero{height:352px;background:linear-gradient(135deg,#b8b8b8 0%,#8d8d8d 45%,#d8d8d8 100%)}

  .feature{padding:40px 40px 0 53px;height:1650px}
  .feature h1{color:var(--green);font-weight:700;font-size:32px;line-height:43px;text-align:center;margin:0 -30px 28px;letter-spacing:-0.3px;white-space:nowrap}
  .feature p{font-size:19.6px;line-height:26.4px;letter-spacing:-0.2px;text-align:justify;text-align-last:center;color:var(--ink-soft);margin-bottom:26px}

  .ribbon{position:relative;height:92px;background:var(--white)}
  .ribbon svg{position:absolute;left:200px;top:-18px}
  .ribbon-label{position:absolute;left:0;right:0;top:4px;text-align:center;color:var(--white);font-weight:700;font-size:31px;letter-spacing:.5px}

  .steps{background:var(--white);height:1215px;position:relative;padding:0 38px 0 53px}
  .steps-line{position:absolute;left:31px;top:18px;width:3px;height:1190px;background:var(--green)}
  .step{position:relative;font-size:19.4px;line-height:26.4px;letter-spacing:-0.2px;text-align:justify;color:var(--ink-soft);margin-bottom:26px}
  .step::before{content:"";position:absolute;left:-30px;top:6px;width:17px;height:17px;border-radius:50%;background:var(--green)}
  .step.last::before{background:#1e1e1e}
  .step b{font-weight:600;color:var(--green-dark)}
  .step strong{font-weight:600;color:var(--ink)}
  .gap{height:40px}

  .showcase{height:392px;background:linear-gradient(var(--white) 0 120px,var(--panel) 120px);position:relative}
  .showcase-screen{position:absolute;left:220px;top:0;width:343px;height:284px;border-radius:8px;background:linear-gradient(180deg,#2b2b2b 0 74%,#d9d9d9 74% 100%)}
  .showcase h2{position:absolute;left:0;right:0;top:326px;text-align:center;color:var(--green);font-weight:700;font-size:31px;line-height:39px}

  .portfolio{padding:32px 0 0 33px;height:615px}
  .epc-table{border-collapse:collapse;width:712px;font-size:16px}
  .epc-table th{background:var(--head-row);font-weight:500;height:47px;color:#333;text-align:left;padding-left:100px;border:1px solid var(--rule)}
  .epc-table th.num{padding-left:8px}
  .epc-table td{height:39px;border:1px solid var(--rule);background:var(--white);font-weight:600;font-size:15px;text-align:center;vertical-align:top;padding-top:4px}
  .epc-table td.rating{width:313px}
  .epc-table td.qty{width:92px}
  .epc-table td.pct{width:104px}
  .epc-table td.risk{width:203px}
  .risk-low{background:var(--lime)!important;color:#c00}
  .risk-mid{background:var(--amber)!important;color:#c00}
  .risk-high{background:var(--red)!important;color:#a00}
  .epc-table td.plain{font-weight:400}

  .contact{height:208px;background:var(--green);color:var(--white);text-align:center;padding-top:28px}
  .contact h3{font-weight:600;font-size:27px;line-height:34px}
  .contact p{font-size:21px;line-height:28px}
  .socials{display:flex;justify-content:center;gap:6px;margin-top:8px}
  .socials span{width:28px;height:28px;border-radius:50%;background:var(--white)}
  .copyright{height:58px;line-height:58px;text-align:center;font-size:14px;color:#777;background:var(--panel)}
</style>
</head>
<body>
<main class="newsletter">

  <header class="masthead">
    <span class="brand-name">Quillmarsh</span>
  </header>

  <div class="hero" role="img" aria-label="Photo of a businessman in a grey suit holding a small black house model showing an A to G energy efficiency rating scale"></div>

  <section class="feature">
    <h1>Setting EPC target to band B, is a start,<br>but there’s still a long way to go</h1>
    <p>There has been much taught about whether tightening the minimum energy efficiency standard of EPC to band ‘B’ by 2030 for commercial properties would unlock economic opportunities for low carbon growth. This forms part of the proposals put forward by the government in October and the input into the consultation on the future of the Minimum Energy Efficiency Standards (MEES) on January 7, 2020</p>
    <p>There is a broad agreement that despite the seemingly lack of enforcement, MEES is having a transformational impact in the market and that a minimum EPC band B target by 2030, expected to cover 85 per cent of the privately rented commercial stock, is the right path. However, there is also a broad acknowledgement that in the context of shifting to a net zero economy by 2050, the current framework does not go far enough as it does not target actual operational energy use and therefore, actual carbon emissions.</p>
    <p>Achieving the target EPC band B will, in most cases, require costly strategies which may be difficult to implement depending on the leasing and refurbishment cycles of an asset. The government estimates that to bring existing commercial buildings up to the target EPC band B by 2030 it would cost £50billion. Under current exemption rules, energy efficiency improvements will only be required if they are deemed to be cost-effective, so not all buildings will be expected to meet the target. These properties will still be lettable providing that landlords can prove that the highest rating has been achieved. In these cases, introducing the requirement to have a minimum (actual) operational energy rating such as a Display Energy Certificate would be a welcomed move that could incentivise interaction between asset owners and occupants, drive energy performance and reduce emissions.</p>
    <p>Addressing the ‘in-use’ performance of commercial buildings can deliver significant energy and carbon savings, and from our own experience at Harlowe we have seen this can be achieved very cost-efficiently.</p>
    <p>For example, the average savings realised on a selection of assets under our management, as part of an advanced data analytics exercise, was 15 per cent, with a ROI of only months. With the support of one of our technical partners, we implemented a combined hardware and software solution that allowed our site teams to uncover opportunities to solve operational issues and improve comfort for occupiers in the areas that really matter.</p>
    <p>Although MEES has promoted the refurbishment of commercial stock with low EPC ratings, it is hard to say whether energy performance in these properties has improved overall. While capital works will be required to improve performance, a lot can be achieved by focusing on the day-to-day operation of buildings – control strategies of HVAC plant, in particular.</p>
  </section>

  <div class="ribbon">
    <svg width="380" height="72" viewBox="0 0 380 72" aria-hidden="true">
      <polygon points="0,44 24,0 356,0 380,44" fill="var(--green)"/>
      <rect x="24" y="0" width="332" height="72" fill="var(--green)"/>
    </svg>
    <div class="ribbon-label">NEXT STEP</div>
  </div>

  <section class="steps">
    <div class="steps-line"></div>
    <p class="step"><b>1.</b> <strong>Prepare an asset schedule</strong> that identifies that EPC status and lease expiry of all properties.</p>
    <p class="step"><b>2. Ensure up to date and accurate EPCs have been prepared.</b> Some of our Clients are taking the opportunity to produce up to date EPCs for their whole portfolio. The majority are identifying and carrying out EPC’s on the priority assets, <strong>e.g. lease expiry by end 2020 with either no current EPC or E, F or G rated, and replacing EPC’s</strong> where specialist advice has shown that the rating can easily be lifted. We have consistently seen over the last few years that one of the main reasons for poor EPC ratings is the inappropriate use of assumptions and default values in the original EPC assessment and modelling process. In many cases, just redoing the EPC properly is lifting the property out of the F and G classes. Quillmarsh recently undertook a review of a portfolio where there were 28 F and G units which, had nothing been done, all would have been unlettable in 2018. By simply re running them (with no cap ex at all) QM lifted all but 1 from F and G’s and lifted 7 to a rating. We have seen this across every portfolio we have been involved in – by rerunning EPC’s we see at least 25% of them lifted with no effort whatsoever.</p>
    <p class="step"><b>3. Ensure all future EPC’s are carried out by an approved assessor</b> (we would recommend that this is the same assessor across all your funds) so that data is all in one place for future modelling, which will become increasingly required and methodology is consistent, who will communicate any issues before EPC’s are lodged and ensure defaults are minimal.</p>
    <p class="step"><b>4. Decide what EPC provisions need to be included in future lease agreements.</b> This might include minimum standards for tenant fit out. Other clients are also considering clauses that explicitly require tenants to maintain minimum EPC ratings or that prohibit them for preparing and lodging their own EPCs for the property they are occupying.</p>
    <div class="gap"></div>
    <p class="step last"><b>5. Finally, start to plan and implement improvement works on the remaining “high risk” EPC’s where ratings have not been improved.</b> Identify the works required to achieve a minimum D or E rating as soon as possible so that site works can be combined with planned upgrade or refurbishment works wherever possible. This planning however cannot start until the review detailed in 2) above is complete, which from experience can take several months.</p>
  </section>

  <section class="showcase">
    <div class="showcase-screen" role="img" aria-label="Desktop monitor showing the portfolio dashboard with summary tiles and an EPC rating bar chart"></div>
    <h2>Sample portfolio Estimated current<br>EPC position based on QM analysis of sites</h2>
  </section>

  <section class="portfolio">
    <table class="epc-table">
      <thead>
        <tr><th>EPC Rating</th><th class="num">Quantity</th><th class="num">Portfolio %</th><th class="num" style="padding-left:80px">Risk %</th></tr>
      </thead>
      <tbody>
        <tr><td class="rating">A</td><td class="qty">5</td><td class="pct">0.17%</td><td class="risk risk-low" rowspan="4">69.94%</td></tr>
        <tr><td class="rating">B</td><td class="qty">133</td><td class="pct">4.64%</td></tr>
        <tr><td class="rating">C</td><td class="qty">905</td><td class="pct">31.56%</td></tr>
        <tr><td class="rating">D</td><td class="qty">963</td><td class="pct">33.58%</td></tr>
        <tr><td class="rating">E</td><td class="qty">526</td><td class="pct">18.34%</td><td class="risk risk-mid">18.34%</td></tr>
        <tr><td class="rating">F</td><td class="qty">193</td><td class="pct">6.73%</td><td class="risk risk-high" rowspan="2">11.72%</td></tr>
        <tr><td class="rating">G</td><td class="qty">143</td><td class="pct">4.99%</td></tr>
        <tr><td></td><td></td><td></td><td></td></tr>
        <tr><td class="rating">TOTAL</td><td class="qty">2868</td><td class="pct">100%</td><td class="risk">100.00%</td></tr>
        <tr><td></td><td></td><td></td><td></td></tr>
        <tr><td></td><td></td><td></td><td></td></tr>
        <tr><td class="rating plain">Not rated</td><td class="qty">2303</td><td></td><td></td></tr>
      </tbody>
    </table>
  </section>

  <footer class="contact">
    <h3>Contact information is</h3>
    <p>Tel:+44 (0) 7700 900 318</p>
    <p>Email: info@quillmarsh.co.uk</p>
    <p>Web: www.quillmarsh.co.uk</p>
    <div class="socials"><span></span><span></span><span></span></div>
  </footer>
  <div class="copyright">© quillmarsh 2019</div>

</main>
</body>
</html>
```